Verpackungsdesign für hochwertiges Haarparfum
Zielgruppe
Tovel's Method ist eine israelische Firma, die hochqualitative Haarprodukte und Haar Tools verkauft. Unsere Zielgruppe sind Frauen, die viel in Ihr Aussehen investieren und auf Ihr Äußeres sehr Wert legen.
Aufgabenstellung
Wir suchen nach einem Design für unsere zwei neuen Haarparfums. Es sollte teuer aussehen und das Design sollte modern und simpel sein. Die Flachen sind mit Milchglas und das Design wird auf die Flaschen gedruckt. Das Design muss komplett in Englischer Sprache sein.
Die Masse sind:
Höhe 7,7 cm
Umfang 11 cm
Es wird zwei Düfte geben.
1. The Nordic : Deckel wird Silber glänzend
2. The Celtic: Deckel wird Silber matt
Informationen die auf der Flasche sein sollten:
1. Firmen Logo (wird angehängt)
2. Name des Parfüms (The Nordic or the Celtic)
3. Longlasting Hair Fragrance
4. 30 ml
5. Includes essential hair vitamins and minerals
6. Alcohol and salt free

```html
<!DOCTYPE html>
<html lang="en">
<head>
<meta charset="utf-8">
<title>Celtic – Longlasting Hair Fragrance Label</title>
<link rel="stylesheet" href="https://fonts.googleapis.com/css2?family=Cinzel:wght@400;500&family=Crimson+Text&family=Pinyon+Script&display=swap">
<style>
  :root {
    --backdrop: #eeeeee;
    --label: #bcbcbc;
    --ink: #141414;
    --gold: #f7c600;
    --gold-soft: #f2cf3a;
  }
  * { margin: 0; padding: 0; box-sizing: border-box; }
  html, body {
    width: 1200px;
    height: 1056px;
    overflow: hidden;
    background: var(--backdrop);
  }
  .canvas {
    position: relative;
    width: 1200px;
    height: 1056px;
  }
  .label {
    position: absolute;
    left: 346px;
    top: 48px;
    width: 508px;
    height: 960px;
    background: var(--label);
    color: var(--ink);
    text-align: center;
  }
  .brand {
    position: absolute;
    top: 130px;
    left: 0;
    width: 100%;
    display: flex;
    justify-content: center;
    align-items: center;
    gap: 10px;
    font-family: "Crimson Text", serif;
    font-size: 20px;
    letter-spacing: 2px;
    text-transform: uppercase;
    color: var(--ink);
  }
  .brand-mark {
    width: 14px;
    height: 14px;
    border: 1.5px solid var(--ink);
  }
  .product-name {
    position: absolute;
    top: 276px;
    left: 0;
    width: 100%;
    font-family: "Cinzel", serif;
    font-weight: 400;
    font-size: 62px;
    line-height: 1;
    color: var(--gold);
  }
  .name-rule {
    position: absolute;
    top: 362px;
    left: 50%;
    width: 286px;
    height: 7px;
    margin-left: -143px;
    border-top: 2px solid var(--ink);
    border-bottom: 2px solid var(--ink);
  }
  .tagline {
    position: absolute;
    top: 424px;
    left: 0;
    width: 100%;
    font-family: "Cinzel", serif;
    font-size: 21px;
    letter-spacing: 0.5px;
  }
  .wreath {
    position: absolute;
    top: 452px;
    left: 50%;
    width: 300px;
    height: 188px;
    margin-left: -150px;
  }
  .script {
    position: absolute;
    left: 0;
    width: 100%;
    font-family: "Pinyon Script", cursive;
    font-size: 40px;
    line-height: 1;
  }
  .script-hair { top: 470px; padding-left: 60px; }
  .script-fragrance { top: 494px; padding-right: 6px; }
  .claims {
    position: absolute;
    left: 0;
    width: 100%;
    font-family: "Crimson Text", serif;
    font-size: 16px;
    line-height: 1.2;
  }
  .claim-vitamins { top: 758px; }
  .claim-free { top: 820px; }
  .volume {
    position: absolute;
    top: 880px;
    left: 0;
    width: 100%;
    font-family: "Crimson Text", serif;
    font-size: 32px;
    line-height: 1;
  }
  .volume-unit { font-size: 14px; letter-spacing: 1px; }
</style>
</head>
<body>
<main class="canvas">
  <section class="label">
    <div class="brand"><span class="brand-mark"></span><span>Tovel's Method</span></div>

    <h1 class="product-name">CELTIC</h1>
    <div class="name-rule"></div>

    <p class="tagline">LONGLASTING</p>

    <svg class="wreath" viewBox="0 0 300 188" role="img" aria-label="Golden laurel wreath ornament framing the product description">
      <path d="M12 4 C0 80 50 160 150 184 C250 160 300 80 288 4 C278 70 230 140 150 160 C70 140 22 70 12 4 Z" fill="var(--gold-soft)"/>
    </svg>

    <p class="script script-hair">Hair</p>
    <p class="script script-fragrance">Fragrance</p>

    <p class="claims claim-vitamins">Includes essential hair<br>vitamins and minerals</p>
    <p class="claims claim-free">Alcohol and salt free</p>

    <p class="volume">30<span class="volume-unit">ML</span></p>
  </section>
</main>
</body>
</html>
```